Gift Cards in the Mail Envelope

Mailing out gift cards in the envelope. Need an eye popping envelope. Please look at the enclosed images. The envelope should look like that.

Low design quality

```html
<!DOCTYPE html>
<html lang="en">
<head>
<meta charset="UTF-8">
<title>Gift Card Envelope</title>
<link href="https://fonts.googleapis.com/css2?family=Montserrat:wght@700;800&display=swap" rel="stylesheet">
<style>
  :root {
    --backdrop: #d9d9d9;
    --pink: #f92a8d;
    --black: #000000;
    --white: #ffffff;
  }
  html, body {
    margin: 0;
    padding: 0;
    overflow: hidden;
  }
  .canvas {
    position: relative;
    width: 1200px;
    height: 1200px;
    background: var(--backdrop);
    font-family: "Montserrat", sans-serif;
    overflow: hidden;
  }
  .envelope-front,
  .envelope-back {
    position: absolute;
    left: 277px;
    width: 646px;
    height: 431px;
    background: var(--pink);
  }
  .envelope-front { top: 154px; }
  .envelope-back { top: 616px; }
  .envelope-front .lower-band {
    position: absolute;
    left: 0;
    top: 215px;
    width: 100%;
    height: 216px;
    background: var(--black);
  }
  .headline {
    position: absolute;
    left: 0;
    width: 100%;
    margin: 0;
    text-align: center;
    line-height: 1;
    font-weight: 800;
    font-size: 80px;
    letter-spacing: -1px;
  }
  .headline-gift { top: 123px; color: var(--black); }
  .headline-card { top: 227px; color: var(--white); }
  .teaser {
    position: absolute;
    left: 0;
    width: 100%;
    margin: 0;
    text-align: center;
    line-height: 1;
    font-weight: 700;
  }
  .teaser-kicker { top: 133px; font-size: 17px; color: var(--black); }
  .teaser-call { top: 149px; font-size: 35px; color: var(--white); }
</style>
</head>
<body>
  <main class="canvas">
    <section class="envelope-front">
      <div class="lower-band"></div>
      <h1 class="headline headline-gift">Gift</h1>
      <h1 class="headline headline-card">Card</h1>
    </section>
    <section class="envelope-back">
      <p class="teaser teaser-kicker">Gift Awaits</p>
      <p class="teaser teaser-call">Open Me</p>
    </section>
  </main>
</body>
</html>
```